Feedback App to request feedback from colleagues

It’s a small web app to collect feedback from team members. This is the general screen flow but happy for variations to it.

Users logs into application and is able to see the feedback received till date from different colleagues.

At the top right are “Request feedback”, “Respond to Feedback”.

When the user clicks on Request Feedback, there are three options.
Adhoc Feedback
Mid Year Feedback
360 Feedback

Adhoc feedback will open a screen where I can search for colleagues to request feedback from (I can select more than one). There are three pre-defined question that can I edit if needed.

Mid year feedback: same process but questions cannot be edited

360 Feedback - just redirect to another website.

Respond to Feedback - see incoming request and the ability to provide feedback to questions received.

Send Feedback: select a colleague and send adhoc feedback.

Colours to be used are white and red only. Simple design, the app will be embedded in a portal so need for headers etc. think of a mobile view but no need for logo, header bar etc

Colour Codes:
Red: #E60000
White #FFFFFF
Grey: #333333 (Only use if needed e.g. borders, background etc)
Black: #000000

Only the above colours to be used

Number of Pages Required

1 page

Font styles to use
Sans Serif

Colors
EB3D1F
EC4F4E
F09395
F8D3D4
FCEDEE

Requirements
Must have
• Design screens for every page mentioned
Nice to have
• Clean design, use of images and icons
Should not have
• Cluttered design, header

```html
<!DOCTYPE html>
<html lang="en">
<head>
<meta charset="utf-8">
<title>Feedback App</title>
<link rel="stylesheet" href="https://fonts.googleapis.com/css2?family=Roboto:wght@300;400;500&family=Lato:wght@400;700&display=swap">
<style>
:root{
  --red:#EB3D1F;
  --pink:#F09395;
  --blush:#F8D3D4;
  --page:#DCDCDC;
  --white:#FFFFFF;
  --ink:#333333;
  --black:#000000;
  --shadow:0 12px 30px rgba(0,0,0,.09);
}
*{box-sizing:border-box;margin:0;padding:0}
html,body{width:1200px;height:2523px;overflow:hidden}
body{background:var(--page);font-family:'Roboto',sans-serif;color:var(--ink);position:relative}
.panel{position:absolute;left:109px;width:983px;background:var(--white)}
.panel--feed{top:80px;height:564px}
.panel--menu{top:721px;height:311px}
.panel--adhoc{top:1118px;height:1325px}

.btn{position:absolute;height:35px;border-radius:18px;font:500 12.5px/35px 'Roboto',sans-serif;color:var(--white);text-align:center;border:2px solid transparent}
.btn--soft{background:var(--pink)}
.btn--solid{background:var(--red)}
.btn--active{border-color:var(--red);box-shadow:0 0 0 1px var(--white) inset}
.header-actions .btn{top:27px;width:172px}
.header-actions .btn--soft{left:539px}
.header-actions .btn--solid{left:721px}

.note{position:absolute;width:255px;height:166px;background:var(--white);box-shadow:var(--shadow)}
.note::after{content:"";position:absolute;left:30px;bottom:-18px;border-left:14px solid transparent;border-right:14px solid transparent;border-top:18px solid var(--white);filter:drop-shadow(0 4px 3px rgba(0,0,0,.04))}
.avatar{position:absolute;border-radius:50%;background:linear-gradient(160deg,#c9c0b8,#8a7f78)}
.note .avatar{left:25px;top:13px;width:49px;height:49px}
.note__name{position:absolute;left:82px;top:30px;font:500 12.5px 'Roboto',sans-serif;color:var(--black)}
.note__text{position:absolute;left:0;right:0;top:70px;text-align:center;font:400 12px/22.5px 'Roboto',sans-serif;color:var(--ink)}

.menu-list{position:absolute;left:552px;top:124px;list-style:none}
.menu-list li{font:500 12.5px 'Roboto',sans-serif;color:var(--black);height:53px}

.tab{position:absolute;top:55px;width:175px;height:37px;border-radius:19px;border:1px solid #cfcfcf;background:var(--white);font:500 12.5px/35px 'Roboto',sans-serif;color:var(--black);text-align:center}
.tab--active{background:var(--pink);color:var(--white);border:2px solid var(--red);line-height:33px}

.search{position:absolute;left:92px;top:162px;width:800px;height:47px;background:var(--white);box-shadow:0 4px 16px rgba(0,0,0,.08);font:400 14px/47px 'Roboto',sans-serif;color:var(--black);padding-left:19px}
.search svg{position:absolute;right:19px;top:17px}

.colleague{position:absolute;left:92px;width:801px;height:172px;background:var(--white);box-shadow:var(--shadow)}
.colleague .avatar{left:49px;top:28px;width:61px;height:61px}
.colleague__name{position:absolute;left:123px;top:25px;font:700 14px 'Lato',sans-serif;color:var(--black)}
.colleague__text{position:absolute;left:123px;top:47px;width:640px;font:400 13.5px/22.5px 'Lato',sans-serif;color:var(--ink)}
.colleague .btn{left:123px;top:109px;width:172px}

.questions-title{position:absolute;left:0;right:0;top:1012px;text-align:center;font:400 32px 'Roboto',sans-serif;color:var(--ink)}
.question{position:absolute;left:92px;width:800px;height:47px;background:var(--white);box-shadow:0 4px 16px rgba(0,0,0,.08);font:400 14px/47px 'Roboto',sans-serif;color:var(--black);padding-left:19px}
.question svg{position:absolute;right:20px;top:17px}
</style>
</head>
<body>

<section class="panel panel--feed">
  <div class="header-actions">
    <div class="btn btn--soft">Request Feedback</div>
    <div class="btn btn--solid">Respond to Feedback</div>
  </div>
  <article class="note" style="left:92px;top:112px"><div class="avatar" role="img" aria-label="Colleague portrait photo"></div><div class="note__name">Jone Deo</div><p class="note__text">Lorem ipsum dolor sit amet, consectetur<br>adipiscing elit, sed do eiusmod tempor<br>incididunt ut labore et dolore magna aliqua<br>enim ad minim veniam quis nostrud</p></article>
  <article class="note" style="left:365px;top:112px"><div class="avatar" role="img" aria-label="Colleague portrait photo" style="background:linear-gradient(160deg,#d8c4bd,#a84a5a)"></div><div class="note__name">Jone Deo</div><p class="note__text">Lorem ipsum dolor sit amet, consectetur<br>adipiscing elit, sed do eiusmod tempor<br>incididunt ut labore et dolore magna aliqua<br>enim ad minim veniam quis nostrud</p></article>
  <article class="note" style="left:638px;top:112px"><div class="avatar" role="img" aria-label="Colleague portrait photo" style="background:linear-gradient(160deg,#d5d5d5,#8d8d8d)"></div><div class="note__name">Jone Deo</div><p class="note__text">Lorem ipsum dolor sit amet, consectetur<br>adipiscing elit, sed do eiusmod tempor<br>incididunt ut labore et dolore magna aliqua<br>enim ad minim veniam quis nostrud</p></article>
  <article class="note" style="left:92px;top:323px"><div class="avatar" role="img" aria-label="Colleague portrait photo" style="background:linear-gradient(160deg,#d3d3d3,#2f3a4a)"></div><div class="note__name">Jone Deo</div><p class="note__text">Lorem ipsum dolor sit amet, consectetur<br>adipiscing elit, sed do eiusmod tempor<br>incididunt ut labore et dolore magna aliqua<br>enim ad minim veniam quis nostrud</p></article>
  <article class="note" style="left:365px;top:323px"><div class="avatar" role="img" aria-label="Colleague portrait photo" style="background:linear-gradient(160deg,#ddd,#5a8bb5)"></div><div class="note__name">Jone Deo</div><p class="note__text">Lorem ipsum dolor sit amet, consectetur<br>adipiscing elit, sed do eiusmod tempor<br>incididunt ut labore et dolore magna aliqua<br>enim ad minim veniam quis nostrud</p></article>
  <article class="note" style="left:638px;top:323px"><div class="avatar" role="img" aria-label="Colleague portrait photo" style="background:linear-gradient(160deg,#ddd,#a9c3d8)"></div><div class="note__name">Jone Deo</div><p class="note__text">Lorem ipsum dolor sit amet, consectetur<br>adipiscing elit, sed do eiusmod tempor<br>incididunt ut labore et dolore magna aliqua<br>enim ad minim veniam quis nostrud</p></article>
</section>

<section class="panel panel--menu">
  <div class="header-actions">
    <div class="btn btn--soft btn--active">Request Feedback</div>
    <div class="btn btn--solid">Respond to Feedback</div>
  </div>
  <ul class="menu-list">
    <li>Adhoc Feedback</li>
    <li>Mid Year Feedback</li>
    <li>360 Feedback</li>
  </ul>
</section>

<section class="panel panel--adhoc">
  <div class="tab tab--active" style="left:203px">Adhoc Feedback</div>
  <div class="tab" style="left:405px">Mid Year Feedback</div>
  <div class="tab" style="left:606px">360 Feedback</div>

  <div class="search">Search
    <svg width="13" height="13" viewBox="0 0 13 13"><circle cx="5.3" cy="5.3" r="4.2" fill="none" stroke="#000" stroke-width="2"/><line x1="8.4" y1="8.4" x2="12" y2="12" stroke="#000" stroke-width="2.2" stroke-linecap="round"/></svg>
  </div>

  <article class="colleague" style="top:239px"><div class="avatar" role="img" aria-label="Colleague portrait photo" style="background:linear-gradient(160deg,#e2e2e2,#8e8e8e)"></div><h3 class="colleague__name">Willam Smith</h3><p class="colleague__text">Lorem ipsum dolor sit amet, consectetur adipiscing elit, sed do eiusmod tempor incididunt ut labore et dolore magna aliqua. Ut enim ad minim veniam, quis nostrud exercitatio</p><div class="btn btn--soft">Request Feedback</div></article>
  <article class="colleague" style="top:432px"><div class="avatar" role="img" aria-label="Colleague portrait photo" style="background:linear-gradient(160deg,#eee,#b58f74)"></div><h3 class="colleague__name">Willam Smith</h3><p class="colleague__text">Lorem ipsum dolor sit amet, consectetur adipiscing elit, sed do eiusmod tempor incididunt ut labore et dolore magna aliqua. Ut enim ad minim veniam, quis nostrud exercitatio</p><div class="btn btn--soft">Request Feedback</div></article>
  <article class="colleague" style="top:625px"><div class="avatar" role="img" aria-label="Colleague portrait photo" style="background:linear-gradient(160deg,#e5e5e5,#5f8fbd)"></div><h3 class="colleague__name">Willam Smith</h3><p class="colleague__text">Lorem ipsum dolor sit amet, consectetur adipiscing elit, sed do eiusmod tempor incididunt ut labore et dolore magna aliqua. Ut enim ad minim veniam, quis nostrud exercitatio</p><div class="btn btn--soft">Request Feedback</div></article>
  <article class="colleague" style="top:818px"><div class="avatar" role="img" aria-label="Colleague portrait photo" style="background:linear-gradient(160deg,#eee,#6b4e40)"></div><h3 class="colleague__name">Willam Smith</h3><p class="colleague__text">Lorem ipsum dolor sit amet, consectetur adipiscing elit, sed do eiusmod tempor incididunt ut labore et dolore magna aliqua. Ut enim ad minim veniam, quis nostrud exercitatio</p><div class="btn btn--soft">Request Feedback</div></article>

  <h2 class="questions-title">Questions</h2>
  <div class="question" style="top:1076px">1.Lorem ipsum dolor sit amet, consectetur adipiscing elit, sed do eiusmod tempor incididunt
    <svg width="12" height="12" viewBox="0 0 12 12"><path d="M1 11 L1.6 8.2 L8.4 1.4 L10.6 3.6 L3.8 10.4 Z" fill="#000"/></svg></div>
  <div class="question" style="top:1142px">2.Lorem ipsum dolor sit amet, consectetur adipiscing elit, sed do eiusmod tempor incididunt
    <svg width="12" height="12" viewBox="0 0 12 12"><path d="M1 11 L1.6 8.2 L8.4 1.4 L10.6 3.6 L3.8 10.4 Z" fill="#000"/></svg></div>
  <div class="question" style="top:1208px">3.Lorem ipsum dolor sit amet, consectetur adipiscing elit, sed do eiusmod tempor incididunt
    <svg width="12" height="12" viewBox="0 0 12 12"><path d="M1 11 L1.6 8.2 L8.4 1.4 L10.6 3.6 L3.8 10.4 Z" fill="#000"/></svg></div>
</section>

</body>
</html>
```